Logo Name:
Rec Center
Company Intro:
The design is for a sign that will direct drivers to various sites in the city.
Instructions:
We need directional signs that are inspired by our other sign concepts (attached). I want to make sure the vine elements on the side are part of the designs. Signs should say "Rec Center" or "Lantern Meadow" with a bold arrow pointing left or right. They should also include an icon that relates to the destination.

```html
<!DOCTYPE html>
<html lang="en">
<head>
<meta charset="utf-8">
<title>Directional Signs – Rec Center &amp; Lantern Meadow</title>
<link href="https://fonts.googleapis.com/css2?family=Fira+Sans+Condensed:wght@600&display=swap" rel="stylesheet">
<style>
  :root {
    --bg: #ffffff;
    --pole: #3a4039;
    --pole-light: #59615a;
    --gold-dark: #a9761f;
    --gold-mid: #c9973f;
    --gold-light: #e0c183;
    --green-dark: #4fa81c;
    --green-mid: #6cc22e;
    --green-light: #a2dc6c;
    --sign-text: #ffffff;
  }
  html, body {
    margin: 0;
    padding: 0;
    width: 1200px;
    height: 900px;
    overflow: hidden;
    background: var(--bg);
  }
  .stage {
    position: relative;
    width: 1200px;
    height: 900px;
    overflow: hidden;
    background: var(--bg);
  }
  .pole {
    position: absolute;
    top: 100px;
    width: 22px;
    height: 800px;
    border-radius: 11px 11px 0 0;
    background: linear-gradient(90deg, var(--pole) 0%, var(--pole-light) 40%, var(--pole) 100%);
  }
  .pole--rec { left: 247px; }
  .pole--meadow { left: 637px; }

  .sign {
    position: absolute;
    top: 118px;
    width: 300px;
    height: 545px;
  }
  .sign--rec { left: 270px; }
  .sign--meadow { left: 662px; }

  .sign__shape {
    position: absolute;
    inset: 0;
    width: 100%;
    height: 100%;
    overflow: visible;
  }
  .sign__title {
    position: absolute;
    left: 0;
    right: 0;
    top: 115px;
    margin: 0;
    text-align: center;
    font-family: "Fira Sans Condensed", "Arial Narrow", sans-serif;
    font-weight: 600;
    font-size: 74px;
    line-height: 76px;
    letter-spacing: 1px;
    color: var(--sign-text);
    text-transform: uppercase;
  }
  .sign--meadow .sign__title {
    font-size: 64px;
    line-height: 76px;
  }
  .sign__row {
    position: absolute;
    left: 0;
    right: 0;
    top: 330px;
    height: 110px;
    display: flex;
    align-items: center;
    justify-content: center;
    gap: 14px;
  }
  .sign__arrow {
    width: 82px;
    height: 64px;
  }
  .sign__icon {
    width: 96px;
    height: 100px;
    border-radius: 14px;
    background: rgba(255, 255, 255, 0.85);
  }
</style>
</head>
<body>
<main class="stage">

  <div class="pole pole--rec"></div>
  <div class="pole pole--meadow"></div>

  <!-- Rec Center sign -->
  <section class="sign sign--rec" aria-label="Rec Center, to the left">
    <svg class="sign__shape" viewBox="0 0 300 545">
      <defs>
        <linearGradient id="gold-fill" x1="0" y1="0" x2="1" y2="1">
          <stop offset="0" stop-color="var(--gold-dark)"/>
          <stop offset="0.45" stop-color="var(--gold-light)"/>
          <stop offset="1" stop-color="var(--gold-dark)"/>
        </linearGradient>
      </defs>
      <rect role="img" aria-label="Curling vine ornament with a leaf" x="20" y="0" width="130" height="95" rx="40" fill="var(--gold-mid)"/>
      <path d="M4 92 Q150 62 296 74 L296 330 Q292 440 150 545 Q8 440 4 330 Z" fill="url(#gold-fill)"/>
    </svg>
    <h2 class="sign__title">Rec<br>Center</h2>
    <div class="sign__row">
      <svg class="sign__arrow" viewBox="0 0 82 64" aria-label="Arrow pointing left">
        <path d="M78 32 H10 M34 8 L10 32 L34 56" fill="none" stroke="var(--sign-text)" stroke-width="11" stroke-linecap="round" stroke-linejoin="round"/>
      </svg>
      <div class="sign__icon" role="img" aria-label="Icon of a tree beside a winding path"></div>
    </div>
  </section>

  <!-- Lantern Meadow sign -->
  <section class="sign sign--meadow" aria-label="Lantern Meadow, to the right">
    <svg class="sign__shape" viewBox="0 0 300 545">
      <defs>
        <linearGradient id="green-fill" x1="0" y1="0" x2="1" y2="1">
          <stop offset="0" stop-color="var(--green-dark)"/>
          <stop offset="0.45" stop-color="var(--green-light)"/>
          <stop offset="1" stop-color="var(--green-dark)"/>
        </linearGradient>
      </defs>
      <rect role="img" aria-label="Curling vine ornament with a leaf" x="20" y="0" width="130" height="95" rx="40" fill="var(--green-mid)"/>
      <path d="M4 92 Q150 62 296 74 L296 330 Q292 440 150 545 Q8 440 4 330 Z" fill="url(#green-fill)"/>
    </svg>
    <h2 class="sign__title">Lantern<br>Meadow</h2>
    <div class="sign__row">
      <div class="sign__icon" role="img" aria-label="Icon for the Lantern Meadow destination"></div>
      <svg class="sign__arrow" viewBox="0 0 82 64" aria-label="Arrow pointing right">
        <path d="M4 32 H72 M48 8 L72 32 L48 56" fill="none" stroke="var(--sign-text)" stroke-width="11" stroke-linecap="round" stroke-linejoin="round"/>
      </svg>
    </div>
  </section>

</main>
</body>
</html>
```